Business card and stationary for eco-aware technology company
Verdalux: Green-minded Scrap Recovery
Business card and stationary for eco-aware technology company - Chemicals
Creative Brief
Professional
Tam Brendow
Managing Director
7-3, 2nd Floor, Pelham Court, Quarry Road, 10450 Georgetown, Penang, Malaysia
+604-8XXXXXX
+6011-5274 XXXX
xxx@verdalux.example
http://www.verdalux.example
YYYYYYY-K
Hello, My name is Tam Brendow, and I am MD of Verdalux. I would like a letterhead and a business card for myself. Verdalux is a Malaysia-based startup with a focus on developing technology for urban mining ( http://scrapharvest.example/ ). Verdalux's name is legally Verdalux Sdn. Bhd., but maybe the shorter form, 'Verdalux' looks better on a business card. Perhaps the "Sdn. Bhd." could be hidden in there somewhere. Up to you! For the business card, the following info should be used: Tam Brendow Managing Director MChem, Ph.D (Chemistry) The back side of the business card can be blank, or it can be very simply decorated. I am on Malaysian time (GMT +8) so please forgive me if my feedback appears delayed. Thanks & good luck, - Tam
Empty is fine. Very simple decoration if you want - maybe just the company logo in the center.
tbrendow tbrendow
Hey, Sorry for the slow feedback. I've just got back to the office. Firstly, I am happy to review the business card designs on this site. However, the stationary designs are too big to preview and quorbasketch's site makes it too slow for me to look at the designs. So, would you designers be able to host the images on a web server, or put them in a .zip file? Private message me the URL and I'll download them and use an image viewer to see them offline. Sorry for the extra work - blame QS's crap design. Ok, now for some feedback: 1) The dark 'Eco' green does not look nice on the card. Please use only a little bit! 2) Lighter greens are nice. Like the colour of the 3 leaves. 3) No transparent cards, please. 4) The back of the card should have a very simple design. Maybe just the 3 leaves on a white background, with no text? 5) I love the designs with the big leaf (#191). It's clever. I also love the designs with the circuit pattern (#212, #213, #214). That's clever too. Private message me if you want more feedback or ideas. I'll try to reply fast. Thanks, - Tam

```html
<!DOCTYPE html>
<html lang="en">
<head>
<meta charset="utf-8">
<title>Verdalux business card</title>
<link href="https://fonts.googleapis.com/css2?family=Source+Sans+3:wght@400;600;700&display=swap" rel="stylesheet">
<style>
  :root {
    --page: #e6e9e7;
    --card: #ffffff;
    --green-deep: #1f6b34;
    --green-mid: #2c8a3e;
    --green-light: #7cc142;
    --brand: #3f9b35;
    --ink-white: #ffffff;
    --ink-soft: #e4f1e2;
  }
  * { margin: 0; padding: 0; box-sizing: border-box; }
  html, body { width: 1200px; height: 780px; overflow: hidden; }
  body {
    background: var(--page);
    font-family: "Source Sans 3", sans-serif;
    position: relative;
  }
  .card {
    position: absolute;
    left: 100px; top: 100px;
    width: 1000px; height: 580px;
    border-radius: 40px;
    overflow: hidden;
    background: var(--card);
    box-shadow: 0 6px 24px rgba(0,0,0,0.12);
  }
  .card-shapes { position: absolute; inset: 0; }
  .brand {
    position: absolute;
    left: 300px; top: 78px;
    display: flex; align-items: center; gap: 18px;
  }
  .brand-dot {
    width: 84px; height: 84px; border-radius: 50%;
    background: var(--green-light);
  }
  .brand-name {
    font-weight: 700; font-size: 88px; line-height: 0.9;
    color: var(--brand); letter-spacing: -1px;
  }
  .brand-tagline {
    font-weight: 600; font-size: 20px; letter-spacing: 3.2px;
    color: var(--brand); margin-top: 4px;
  }
  .divider {
    position: absolute; left: 536px; top: 300px;
    width: 2px; height: 250px; background: rgba(255,255,255,0.55);
  }
  .person {
    position: absolute; right: 490px; top: 318px;
    text-align: right; color: var(--ink-white);
  }
  .person-name { font-weight: 600; font-size: 32px; line-height: 1.1; }
  .person-degree { font-weight: 700; font-size: 20px; margin-top: 4px; }
  .person-role { font-size: 21px; margin-top: 2px; }
  .address {
    font-size: 19px; line-height: 1.45; margin-top: 30px; color: var(--ink-soft);
  }
  .contacts {
    position: absolute; left: 564px; top: 286px;
    color: var(--ink-white); font-size: 20px; list-style: none;
  }
  .contacts li { display: flex; align-items: center; gap: 14px; height: 34px; }
  .contacts .license { height: 40px; }
  .contacts svg { width: 20px; height: 20px; flex: none; }
</style>
</head>
<body>
  <div class="card">
    <svg class="card-shapes" viewBox="0 0 1000 580" preserveAspectRatio="none" aria-hidden="true">
      <path d="M0 262 C 240 320, 560 330, 1000 222 L1000 580 L0 580 Z" fill="var(--green-light)"/>
      <path d="M0 276 C 240 336, 560 344, 1000 238 L1000 580 L0 580 Z" fill="var(--green-mid)"/>
      <path d="M0 296 C 260 352, 580 360, 1000 262 L1000 580 L0 580 Z" fill="var(--green-deep)"/>
    </svg>

    <div class="brand">
      <span class="brand-dot"></span>
      <div>
        <div class="brand-name">Verdalux</div>
        <div class="brand-tagline">GREEN-MINDED SCRAP RECOVERY</div>
      </div>
    </div>

    <div class="divider"></div>

    <div class="person">
      <div class="person-name">Tam Brendow</div>
      <div class="person-degree">MChem, Ph.D (Chemistry)</div>
      <div class="person-role">Managing Director</div>
      <div class="address">
        7-3, 2nd Floor, Pelham Court<br>
        Quarry Road, 10450 Georgetown<br>
        Penang, Malaysia
      </div>
    </div>

    <ul class="contacts">
      <li class="license">License No YYYYYYY-K</li>
      <li>
        <svg viewBox="0 0 20 20"><path fill="#fff" d="M2 7c0-3 3-4 8-4s8 1 8 4l-3 1-1-2H6L5 8zM5 9h10l2 8H3z"/></svg>
        604-8XXXXXX
      </li>
      <li>
        <svg viewBox="0 0 20 20"><rect x="5" y="1" width="10" height="18" rx="2" fill="#fff"/><rect x="7" y="3" width="6" height="11" fill="var(--green-deep)"/></svg>
        6011-5274 XXXX
      </li>
      <li>
        <svg viewBox="0 0 20 20"><rect x="5" y="2" width="10" height="6" fill="#fff"/><rect x="1" y="8" width="18" height="9" rx="2" fill="#fff"/><rect x="5" y="12" width="10" height="2" fill="var(--green-deep)"/></svg>
        604-8XXXXYY
      </li>
      <li>
        <svg viewBox="0 0 20 20"><rect x="1" y="4" width="18" height="12" rx="2" fill="#fff"/><path d="M2 5l8 6 8-6" stroke="var(--green-deep)" stroke-width="1.6" fill="none"/></svg>
        info@verdalux.example
      </li>
      <li>
        <svg viewBox="0 0 20 20"><circle cx="10" cy="10" r="8.5" fill="#fff"/><path d="M2 10h16M10 2c-4 4-4 12 0 16M10 2c4 4 4 12 0 16" stroke="var(--green-deep)" stroke-width="1.3" fill="none"/></svg>
        www.verdalux.example
      </li>
    </ul>
  </div>
</body>
</html>
```